Design for new site

Hi, we need a web design for a new product calmridgeway.
This product is aimed to help people with anxiety, panic attacks and other disorders on permanently basis.
Please take a look at competitors web-sites:
http://www.brightharborpath.example/
http://www.stillmeadow.example/
Key Audiences
The intended audience for this site will be people that are looking for relief from panic and anxiety.
Key Objectives
Key object is to get prospective clients to sign up for membership and purchase our audio course.
Theme of Site
The general site theme needs to be clean and simple. The audience coming to the site in under a lot of anxiety and we don’t want to add any stress.
The site needs to flow easy from top down, with few distractions in side menus and/or columns.
Color Scheme
Suggested colors need to be light shades of blue. Blue psychology is tranquil, peaceful, and calm. This color has a tremendous stress management quality to it, making us feel cool and calm.
Or it can be shades of cool green of summer forest.
Please take a look at site mock up in attachment.

```html
<!DOCTYPE html>
<html lang="en">
<head>
<meta charset="utf-8">
<title>calmridgeway</title>
<link href="https://fonts.googleapis.com/css2?family=Open+Sans:ital,wght@0,400;0,600;0,700;1,400&display=swap" rel="stylesheet">
<style>
:root{
  --sky:#36c9fb;
  --panel:#1ab4ea;
  --ribbon:#1585b3;
  --deep:#1f8fc4;
  --link:#2a9bd3;
  --text:#555;
  --muted:#777;
  --rule:#cfcfcf;
  --footer:#454545;
  --white:#fff;
}
*{box-sizing:border-box;margin:0;padding:0}
html,body{width:891px;height:1200px;overflow:hidden}
body{position:relative;background:var(--white);font-family:"Open Sans",Arial,sans-serif;color:var(--text)}
.abs{position:absolute}

.site-header{position:absolute;left:0;top:0;width:891px;height:88px;background:var(--sky)}
.brand{position:absolute;left:88px;top:30px;display:flex;align-items:center;gap:8px;color:var(--white);font-size:20px;font-weight:600}
.brand-mark{width:16px;height:16px;background:var(--white)}
.main-nav{position:absolute;left:324px;top:37px;display:flex;font-size:11px;font-weight:600;color:var(--white)}
.main-nav span{height:21px;line-height:21px;padding:0 6px;margin-right:2px;white-space:nowrap}
.main-nav .current{background:var(--deep)}
.caret{font-size:7px;opacity:.8;margin-left:3px}

.hero-image{left:87px;top:99px;width:496px;height:256px;background:linear-gradient(100deg,#e3e3e3 0%,#c9302a 25%,#d9b72e 32%,#4cc81f 50%,#2f9e1c 60%,#1f48c9 75%,#e9e9e9 100%)}
.slider-arrow{top:192px;width:38px;height:38px}
.signup{left:583px;top:98px;width:216px;height:264px;background:var(--panel);color:var(--white)}
.signup-ribbon{position:absolute;left:7px;top:10px;width:220px;height:37px;background:var(--ribbon);text-align:center;line-height:37px;font-size:17px;font-weight:700}
.signup-fold{position:absolute;left:215px;top:47px}
.signup-intro{position:absolute;left:21px;top:62px;width:180px;font-size:11.5px;line-height:15px}
.field{position:absolute;left:19px;width:168px;height:25px;background:#f4f4f4;color:#999;font-style:italic;font-size:10px;line-height:25px;padding-left:8px}
.submit{position:absolute;left:20px;top:199px;width:79px;height:30px;background:var(--deep);border-bottom:2px solid #157199;font-weight:700;font-size:14px;text-align:center;line-height:28px}

.welcome{left:0;top:401px;width:891px;text-align:center;font-size:19px;color:#444}
.welcome b{color:var(--link);font-weight:600;margin-left:6px}
.intro{left:125px;width:641px;text-align:center;font-size:12.5px;line-height:16px;color:#666}

.section-title{font-size:17px;font-weight:600;color:var(--link)}
.rule{height:1px;background:var(--rule)}
.mini-arrows{display:flex;gap:3px}
.mini-arrows i{width:15px;height:15px;border-radius:50%;background:#a9a9a9;display:block;position:relative}
.mini-arrows i::after{content:"";position:absolute;left:5px;top:4px;border:3.5px solid transparent}
.mini-arrows .prev::after{border-right:4px solid #fff;left:2px}
.mini-arrows .next::after{border-left:4px solid #fff;left:6px}

.blog-photo{left:88px;top:652px;width:176px;height:134px;background:linear-gradient(160deg,#6d5a48,#8aa65a 55,#5d7a42)}
.blog-title{left:290px;top:649px;font-size:17px;color:var(--link)}
.blog-text{left:290px;top:676px;width:215px;font-size:11.5px;line-height:19.2px;color:#777}

.news{left:574px;top:621px;width:218px;height:182px;background:#f7f7f7;border:1px solid #e2e2e2;box-shadow:0 4px 6px -4px rgba(0,0,0,.25)}
.news-head{height:38px;background:var(--deep);color:var(--white);font-size:16px;font-weight:600;text-align:center;line-height:38px}
.news-item{position:absolute;left:8px;width:195px;height:60px}
.news-thumb{position:absolute;left:0;top:6px;width:42px;height:40px;background:linear-gradient(#e9eef2,#c9d4dc);border:2px solid #fff;box-shadow:0 1px 2px rgba(0,0,0,.3)}
.news-title{position:absolute;left:54px;top:0;font-size:10px;color:var(--link)}
.news-text{position:absolute;left:54px;top:15px;width:130px;font-size:6px;line-height:8.4px;color:#888}
.news-text em{color:var(--link);font-style:normal;font-weight:600}

.small-copy{font-size:8px;line-height:15px;color:#777}
.small-copy a{color:var(--link);text-decoration:underline}
.nl-copy{left:318px;top:907px;width:205px;font-size:11.5px;line-height:15px;color:#666}
.nl-copy span{color:var(--link)}
.nl-field{left:319px;width:189px;height:25px;border:1px solid var(--sky);font-size:9px;font-style:italic;color:#888;line-height:23px;padding-left:9px}
.nl-field svg{position:absolute;right:9px;top:6px}
.subscribe{left:319px;top:1050px;width:72px;height:24px;background:var(--sky);color:var(--white);font-size:12px;font-weight:600;text-align:center;line-height:24px}

.avatar{width:44px;height:44px;border-radius:50%;background:linear-gradient(#eee,#b9b9b9);border:2px solid #fff;box-shadow:0 0 2px rgba(0,0,0,.4)}
.quote-mark{font-size:14px;font-weight:700;color:var(--link);line-height:1}
.quote{width:118px;font-family:Georgia,serif;font-style:italic;font-size:7.2px;line-height:10.5px;color:#888}
.quote-by{font-size:7px;color:#555}
.quote-by span{color:var(--link)}

.site-footer{left:0;top:1123px;width:891px;height:77px;background:var(--footer);color:var(--white)}
.foot-nav{position:absolute;left:87px;top:22px;display:flex;gap:14px;font-size:11px;font-weight:600}
.copyright{position:absolute;left:87px;top:44px;font-size:9px;color:#ddd}
.social{position:absolute;top:23px;width:25px;height:25px;border-radius:50%;border:1.5px solid #eee}
</style>
</head>
<body>

<header class="site-header">
  <div class="brand"><span class="brand-mark"></span>calmridgeway</div>
  <nav class="main-nav">
    <span class="current">Home</span>
    <span>Product<span class="caret">▼</span></span>
    <span style="margin-left:4px">Success Stories<span class="caret">▼</span></span>
    <span style="margin-left:4px">Anxiety Test</span>
    <span>Blog</span>
    <span>About</span>
    <span>FAQ</span>
    <span>Contact Us</span>
  </nav>
</header>

<div class="abs hero-image" role="img" aria-label="Promotional image of three coloured boxes with a best-buy badge"></div>
<svg class="abs slider-arrow" style="left:36px" viewBox="0 0 38 38"><circle cx="19" cy="19" r="17.5" fill="#fff" stroke="#ccc" stroke-width="2"/><path d="M24 10 12 19l12 9-4-9z" fill="#ccc"/></svg>
<svg class="abs slider-arrow" style="left:803px" viewBox="0 0 38 38"><circle cx="19" cy="19" r="17.5" fill="#fff" stroke="#ccc" stroke-width="2"/><path d="M14 10l12 9-12 9 4-9z" fill="#ccc"/></svg>

<aside class="abs signup">
  <div class="signup-ribbon">Sign Up Now!</div>
  <svg class="signup-fold" width="12" height="12" viewBox="0 0 12 12"><path d="M0 0h12L0 12z" fill="#0e5f82"/></svg>
  <p class="signup-intro">Lorem ipsum dolor sit amet, consectetur adipisicing.</p>
  <div class="field" style="top:119px">Enter your name</div>
  <div class="field" style="top:154px">Enter your Email</div>
  <div class="submit">Submit</div>
</aside>

<h1 class="abs welcome" style="font-weight:400">Welcome to<b>CALMRIDGEWAY</b></h1>
<p class="abs intro" style="top:447px">Lorem ipsum dolor sit amet, consectetur adipisicing elit, sed do eiusmod tempor incididunt ut labore et dolore magna aliqua. Ut enim ad minim veniam, quis nostrud exercitation ullamco laboris nisi ut aliquip ex ea commodo consequat. Duis aute irure dolor in repre.</p>
<p class="abs intro" style="top:511px">Henderit in voluptate velit esse cillum dolore eu fugiat nulla pariatur. Excepteur sint occaecat cupidatat non proident, sunt in culpa qui officia deserunt mollit anim id est laborum. Sed ut perspiciatis unde omnis iste natus error sit voluptatem accusantium doloremque laudantium.</p>

<h2 class="abs section-title" style="left:88px;top:608px">Blog</h2>
<div class="abs mini-arrows" style="left:477px;top:623px"><i class="prev"></i><i class="next"></i></div>
<div class="abs rule" style="left:88px;top:640px;width:443px"></div>
<div class="abs blog-photo" role="img" aria-label="Photo of an older man sitting on a garden bench"></div>
<h3 class="abs blog-title" style="font-weight:400">Title of article here</h3>
<p class="abs blog-text">Consectetur adipisicing elit, sed do eiusmod tempor incididunt ut labore et dolore magna aliqua. Ut enim ad minim veniam, quis nostrud exercita tion ullamco laboris nisi ut aliquip ex ea commodo.</p>

<section class="abs news">
  <div class="news-head">Latest News &amp; Events</div>
  <div class="news-item" style="top:54px">
    <div class="news-thumb" role="img" aria-label="Photo of two medical staff"></div>
    <div class="news-title">Lorem ipsum doloreum</div>
    <p class="news-text">Lorem ipsum dolor sit amet, consectetur adipisicing elit, sed do eiusmod tempor incididunt ut labore et dol.. <em>[Read More]</em></p>
  </div>
  <div class="abs rule" style="left:9px;top:107px;width:195px"></div>
  <div class="news-item" style="top:122px">
    <div class="news-thumb" role="img" aria-label="Photo of two medical staff"></div>
    <div class="news-title">Lorem ipsum doloreum</div>
    <p class="news-text">Lorem ipsum dolor sit amet, consectetur adipisicing elit, sed do eiusmod tempor incididunt ut labore et dol.. <em>[Read More]</em></p>
  </div>
</section>

<h2 class="abs section-title" style="left:90px;top:857px">FAQ</h2>
<div class="abs rule" style="left:90px;top:891px;width:148px"></div>
<p class="abs small-copy" style="left:92px;top:904px;width:150px">Lorem ipsum dolor sit amet, consectetur adipisicing elit, sed do eiusmod tempor incididunt ut labore et dolore magna aliqua. Ut enim ad minim veniam, quis.. <a>Read More</a></p>
<div class="abs rule" style="left:90px;top:996px;width:148px"></div>
<p class="abs small-copy" style="left:92px;top:1006px;width:150px">Lorem ipsum dolor sit amet, consectetur adipisicing elit, sed do eiusmod tempor incididunt ut labore et dolore magna aliqua. Ut enim ad minim veniam, quis.. <a>Read More</a></p>
<div class="abs rule" style="left:90px;top:1089px;width:148px"></div>

<h2 class="abs section-title" style="left:319px;top:857px">Newsletter</h2>
<div class="abs rule" style="left:319px;top:891px;width:199px"></div>
<p class="abs nl-copy">Sign up to our newsletter to receive discounts, news, and updates from <span>calmridgeway</span></p>
<div class="abs nl-field" style="top:965px">Name<svg width="10" height="10" viewBox="0 0 10 10"><circle cx="5" cy="3" r="2.5" fill="#bbb"/><path d="M0 10c0-4 10-4 10 0z" fill="#bbb"/></svg></div>
<div class="abs nl-field" style="top:1000px">Email<svg width="11" height="9" viewBox="0 0 11 9"><rect width="11" height="9" fill="#bbb"/><path d="M0 0l5.5 5L11 0" fill="none" stroke="#fff"/></svg></div>
<div class="abs subscribe">Subscribe</div>

<h2 class="abs section-title" style="left:574px;top:857px">Testimonials</h2>
<div class="abs mini-arrows" style="left:757px;top:863px"><i class="prev"></i><i class="next"></i></div>
<div class="abs rule" style="left:572px;top:891px;width:219px"></div>
<div class="abs avatar" style="left:574px;top:909px" role="img" aria-label="Portrait of a customer"></div>
<div class="abs quote-mark" style="left:624px;top:906px">“</div>
<p class="abs quote" style="left:638px;top:911px">Lorem ipsum dolor sit amet, consectetur adipisicing elit, sed do eiusmod tempor incididunt ut.</p>
<p class="abs quote-by" style="left:685px;top:947px"><span>John Doe</span>, New York</p>
<div class="abs rule" style="left:572px;top:972px;width:186px"></div>
<div class="abs avatar" style="left:574px;top:997px" role="img" aria-label="Portrait of a customer"></div>
<div class="abs quote-mark" style="left:624px;top:994px">“</div>
<p class="abs quote" style="left:638px;top:999px">Lorem ipsum dolor sit amet, consectetur adipisicing elit, sed do eiusmod tempor incididunt ut.</p>
<p class="abs quote-by" style="left:685px;top:1036px"><span>Jenna Doe</span>, New York</p>
<div class="abs rule" style="left:572px;top:1060px;width:186px"></div>

<footer class="abs site-footer">
  <nav class="foot-nav"><span>Home</span><span>Product</span><span>Success Stories</span><span>Anxiety Test</span><span>Blog</span><span>About</span><span>FAQ</span><span>Contact Us</span></nav>
  <p class="copyright">Copyright©2014Anxiety project. All Rights Reserved</p>
  <span class="social" style="left:652px"></span>
  <span class="social" style="left:689px"></span>
  <span class="social" style="left:727px"></span>
  <span class="social" style="left:765px"></span>
</footer>

</body>
</html>
```